Update New Business Card - For Start Up

I need to update my business card, I have our old version for example. I would like to keep to the same colors and theme. We are a threat reporting and case management tool for corporations and educational institutions.

Target Market(s)

Corporate Security and Human Resources, School Administrators and Superintendents.

Industry/Entity Type

Physical Security and Technology.

Contact Information for Business Card

My Name, Founder/CEO, phone number 555-214-6082, Logo, Web...

Colors
0054AA
0677BA
7BADD7
CADEEF
E8F1F8

Requirements
Must have
• Something new and trendy.

```html
<!DOCTYPE html>
<html lang="en">
<head>
<meta charset="utf-8">
<title>Vantrel Business Card</title>
<link href="https://fonts.googleapis.com/css2?family=Lato:wght@400;700&display=swap" rel="stylesheet">
<style>
  :root {
    --brand-blue: #1e76bb;
    --ink-grey: #555555;
    --card-white: #ffffff;
    --backdrop: #c9c4c4;
  }
  * { margin: 0; padding: 0; box-sizing: border-box; }
  html, body {
    width: 1200px; height: 1200px; overflow: hidden;
    background: var(--backdrop);
    font-family: "Lato", sans-serif;
  }
  .canvas { position: relative; width: 1200px; height: 1200px; }
  .card {
    position: absolute; left: 229px; width: 744px; height: 420px;
  }
  .card--front { top: 163px; background: var(--card-white); }
  .card--back { top: 620px; height: 415px; background: var(--brand-blue); }

  .brand { position: absolute; left: 64px; top: 57px; height: 128px; display: flex; align-items: center; }
  .brand__dot { width: 128px; height: 128px; border-radius: 50%; background: var(--brand-blue); }
  .brand__name {
    margin-left: 17px; font-weight: 400; font-size: 66px; letter-spacing: 14px;
    color: var(--brand-blue); line-height: 1;
  }
  .card--back .brand { top: 55px; }
  .card--back .brand__dot { background: var(--card-white); }
  .card--back .brand__name { color: var(--card-white); }

  .person { position: absolute; right: 386px; top: 285px; text-align: right; }
  .person__name { font-weight: 700; font-size: 22px; color: var(--brand-blue); letter-spacing: 0.2px; }
  .person__role { margin-top: 8px; font-size: 18px; color: var(--ink-grey); }

  .divider { position: absolute; left: 383px; top: 264px; width: 2px; height: 99px; background: var(--brand-blue); }

  .contacts { position: absolute; left: 411px; top: 260px; list-style: none; }
  .contacts__item {
    display: flex; align-items: center; height: 27.7px;
    font-size: 18px; color: var(--ink-grey);
  }
  .contacts__icon { width: 16px; height: 16px; margin-right: 5px; fill: var(--brand-blue); flex: none; }
</style>
</head>
<body>
<div class="canvas">
  <section class="card card--front">
    <div class="brand">
      <div class="brand__dot"></div>
      <div class="brand__name">VANTREL</div>
    </div>

    <div class="person">
      <div class="person__name">DANA WHITLOW</div>
      <div class="person__role">Founder/CEO</div>
    </div>

    <div class="divider"></div>

    <ul class="contacts">
      <li class="contacts__item">
        <svg class="contacts__icon" viewBox="0 0 16 16" aria-hidden="true"><path d="M3.2 1.5l2.4 2.6-1.3 1.7c.9 2 2.4 3.6 4.4 4.6l1.7-1.3 2.6 2.3-1.4 2.4C6.4 13.4 2.4 9.4 1.2 3z"/><path d="M9.5 2.5a4 4 0 0 1 4 4h-1.2a2.8 2.8 0 0 0-2.8-2.8zM9.5 0a6.5 6.5 0 0 1 6.5 6.5h-1.2A5.3 5.3 0 0 0 9.5 1.2z"/></svg>
        555-214-6082
      </li>
      <li class="contacts__item">
        <svg class="contacts__icon" viewBox="0 0 16 16" aria-hidden="true"><path d="M4.5 0h7a1.5 1.5 0 0 1 1.5 1.5v13a1.5 1.5 0 0 1-1.5 1.5h-7A1.5 1.5 0 0 1 3 14.5v-13A1.5 1.5 0 0 1 4.5 0zm.2 1.8v10.6h6.6V1.8zM8 13.2a.9.9 0 1 0 0 1.8.9.9 0 0 0 0-1.8z"/></svg>
        555-387-1940
      </li>
      <li class="contacts__item">
        <svg class="contacts__icon" viewBox="0 0 16 16" aria-hidden="true"><path d="M1 4h14v1.2L8 9.5 1 5.2z"/><path d="M1 6.8l7 4.3 7-4.3V13H1z"/></svg>
        dana@vantrel.co
      </li>
      <li class="contacts__item">
        <svg class="contacts__icon" viewBox="0 0 16 16" aria-hidden="true"><path d="M8 .5a7.5 7.5 0 1 0 0 15 7.5 7.5 0 0 0 0-15zm-1 2.2c.4.8-.8 1.6-.3 2.5.6 1 2 .6 2.4 1.7.4 1.2-.9 1.8-.6 3 .3 1.1 1.5 1.4 1.4 2.6-.1.8-.8 1.3-1.5 1.4A6.2 6.2 0 0 1 2.3 5.4c1.4-.2 2.1 1 3.1.6.8-.4.6-1.8 1.6-3.3zm4.6 1.2A6.2 6.2 0 0 1 14 8.6c-.8.3-1.8-.2-2-1.2-.3-1.1.6-2.1-.4-3.5z"/></svg>
        www.vantrel.co
      </li>
    </ul>
  </section>

  <section class="card card--back">
    <div class="brand">
      <div class="brand__dot"></div>
      <div class="brand__name">VANTREL</div>
    </div>
  </section>
</div>
</body>
</html>
```